Business card design needed

I am a free lance management consultant looking to have some professionally designed business cards created.
If possible if i could have some bullet points or something with a list of my services that would be great.
Services are:
- Strategic Planning
- Process Improvement
- Change Management
- IT Solutions & Implementation
- IT Consulting
- Web Solutions
Target Market(s)
Business Owners and Operators
Industry/Entity Type
Business
Contact Information for Business Card
Colin Hartley
CH Consulting
0456 318 240
COLIN@COLINHARTLEY.CO
www.colinhartley.co
Logo Text
CH Consulting
Logo styles of interest
Pictorial/Combination Logo
Wordmark Logo
Lettermark Logo

```html
<!DOCTYPE html>
<html lang="en">
<head>
<meta charset="utf-8">
<title>CH Consulting — Business Card</title>
<link href="https://fonts.googleapis.com/css2?family=Arimo:wght@400;700&display=swap" rel="stylesheet">
<style>
  :root {
    --brand-blue: #0a56a0;
    --deep-blue: #123f8f;
    --mark-blue: #1f7cc4;
    --sky-blue: #a6d8f4;
    --card-white: #ffffff;
    --page-bg: #ffffff;
    --edge-grey: #d9d9d9;
    --url-grey: #2e4f86;
  }
  * { margin: 0; padding: 0; box-sizing: border-box; }
  html, body {
    width: 1200px;
    height: 398px;
    overflow: hidden;
    background: var(--page-bg);
    font-family: "Arimo", Arial, sans-serif;
  }
  .sheet {
    position: relative;
    width: 1200px;
    height: 398px;
  }
  .card {
    position: absolute;
    top: 18px;
    width: 567px;
    height: 354px;
    overflow: hidden;
    border: 1px solid var(--edge-grey);
  }

  /* Back side: services */
  .card--services {
    left: 25px;
    background: var(--brand-blue);
  }
  .services-burst {
    position: absolute;
    left: 0;
    top: 0;
    width: 180px;
    height: 100%;
    background: radial-gradient(ellipse at 100% 50%, rgba(166,216,244,0.05) 0%, rgba(166,216,244,0.35) 55%, rgba(255,255,255,0.55) 100%);
  }
  .services-band {
    position: absolute;
    left: 190px;
    right: 0;
    top: 98px;
    height: 158px;
    background: linear-gradient(90deg, rgba(255,255,255,0) 0%, rgba(255,255,255,0.12) 35%, rgba(255,255,255,0.28) 100%);
  }
  .services-list {
    position: absolute;
    left: 206px;
    top: 106px;
    list-style: none;
    color: var(--card-white);
    font-weight: 700;
    font-size: 19px;
    line-height: 23.5px;
  }

  /* Front side: identity */
  .card--identity {
    left: 605px;
    background: var(--card-white);
  }
  .identity-burst {
    position: absolute;
    top: 0;
    height: 100%;
    background: linear-gradient(180deg, rgba(166,216,244,0.55), rgba(166,216,244,0.85) 50%, rgba(166,216,244,0.55));
  }
  .identity-burst--left {
    left: 0;
    width: 128px;
    -webkit-mask: linear-gradient(90deg, #000 40%, transparent);
            mask: linear-gradient(90deg, #000 40%, transparent);
  }
  .identity-burst--right {
    right: 0;
    width: 115px;
    -webkit-mask: linear-gradient(270deg, #000 40%, transparent);
            mask: linear-gradient(270deg, #000 40%, transparent);
  }
  .identity-mark {
    position: absolute;
    left: 209px;
    top: 75px;
    width: 148px;
    height: 148px;
  }
  .identity-name {
    position: absolute;
    left: 0;
    right: 0;
    top: 238px;
    text-align: center;
    color: var(--deep-blue);
    font-weight: 700;
    text-transform: uppercase;
  }
  .identity-name__main {
    display: block;
    font-size: 21px;
    line-height: 24px;
    letter-spacing: 0.5px;
  }
  .identity-name__sub {
    display: block;
    font-size: 13px;
    line-height: 16px;
    letter-spacing: 5px;
    margin-top: 1px;
    padding-left: 5px;
  }
  .identity-url {
    position: absolute;
    left: 0;
    right: 0;
    top: 318px;
    text-align: center;
    font-size: 10px;
    letter-spacing: 0.6px;
    color: var(--url-grey);
  }
</style>
</head>
<body>
  <main class="sheet">
    <section class="card card--services" aria-label="Card back with list of services">
      <div class="services-burst" role="img" aria-label="Decorative radiating pattern of light blue and white bars"></div>
      <div class="services-band"></div>
      <ul class="services-list">
        <li>- Strategic Planning</li>
        <li>- Process Improvement</li>
        <li>- Change Management</li>
        <li>- IT Solutions &amp; Implementation</li>
        <li>- IT Consulting</li>
        <li>- Web Solution</li>
      </ul>
    </section>

    <section class="card card--identity" aria-label="Card front with company name">
      <div class="identity-burst identity-burst--left" role="img" aria-label="Decorative pale blue radiating bars"></div>
      <div class="identity-burst identity-burst--right" role="img" aria-label="Decorative pale blue radiating bars"></div>
      <svg class="identity-mark" viewBox="0 0 148 148" aria-hidden="true">
        <circle cx="74" cy="74" r="64" fill="none" stroke="var(--mark-blue)" stroke-width="16"/>
      </svg>
      <h1 class="identity-name">
        <span class="identity-name__main">Colin Hartley</span>
        <span class="identity-name__sub">Consulting</span>
      </h1>
      <p class="identity-url">www.colinhartley.co</p>
    </section>
  </main>
</body>
</html>
```